Dog Snacks brand needs a new packaging design

Dear Designers,

We are looking for a packaging expert to design our new line of Dog Snacks which contain a relaxing hemp extract (CBD).

Our company is already selling various relaxing cat & dog products , and we would like this new design to reflect the same "style & feeling" as our current products (see attached instructions).

Technical aspects:
- The packaging is a Stand Up Pouch (12x18.5x7cm - see attached instructions).
- Please follow technical guidelines from printer (see attached instructions).
- The packaging will contain 120g of high-quality, semi-moist dog snacks.
- We will be designing 3 differents variations for 3 different flavours: Chicken, Beef & Liver.
- The packaging will be printed with a matt finish.

Design aspects:
- The design should be compatible with our brand identity (i.e. fluffly, pure, relaxing, positive, clean & natural).
- Soft/rounded shapes are preferred.
- Please use our brand's colors (#3BA384, White & Black).
- Please use our company logo (see attached instructions).
- The design also needs to convey a strong sense of professionalism as we are an animal "healthcare" brand.
- If you want to include a dog picture, we would prefer you to use a picture of our official brand ambassador (see attached instructions).
- We have attached a number of packaging examples which we like a lot. (see attached instructions). Please only use those as general inspiration.
- Only original work (no plagiarism will be accepted).

Please don't hesitate to send us a message if you have any questions about the brand, the product or the design requirements.

We look forward to seeing your designs & working on this together !

Thanks & regards,
Marcus

Dog owners

Pet Care

Sans Serif

• Please see project description.

```html
<!DOCTYPE html>
<html lang="en">
<head>
<meta charset="utf-8">
<title>PawVita CBD Treats – Pouch Front</title>
<link rel="stylesheet" href="https://fonts.googleapis.com/css2?family=Roboto:wght@400;500;700&family=Cormorant+Garamond:wght@500;600&display=swap">
<style>
  :root {
    --brand-green: #3ba384;
    --deep-green: #2a8a6c;
    --white: #ffffff;
    --ink: #1d1d1d;
    --silver-light: #f4f4f4;
    --silver-mid: #d9d9d9;
    --silver-dark: #b8b8b8;
    --page: #ffffff;
  }
  * { margin: 0; padding: 0; box-sizing: border-box; }
  html, body { width: 1200px; height: 1200px; overflow: hidden; background: var(--page); }
  .canvas { position: relative; width: 1200px; height: 1200px; }

  .pouch {
    position: absolute; left: 320px; top: 110px; width: 560px; height: 960px;
    border-radius: 10px 10px 18px 18px;
    background: linear-gradient(90deg, var(--silver-dark) 0%, var(--silver-light) 18%, var(--white) 45%, var(--silver-mid) 75%, var(--silver-light) 92%, var(--silver-dark) 100%);
    font-family: "Roboto", sans-serif;
    overflow: hidden;
  }
  .hang-hole {
    position: absolute; left: 270px; top: 20px; width: 20px; height: 20px;
    border-radius: 50%; background: var(--page); border: 2px solid var(--silver-dark);
  }
  .zip-line {
    position: absolute; left: 0; right: 0; top: 80px; height: 3px;
    background: var(--silver-dark); opacity: .6;
  }
  .brand-band {
    position: absolute; left: 0; right: 0; top: 122px; height: 60px;
    background: var(--brand-green);
    display: flex; align-items: center; justify-content: center;
  }
  .brand-name { color: var(--white); font-weight: 700; font-size: 44px; letter-spacing: .5px; }

  .thc-badge { position: absolute; left: 228px; top: 196px; width: 130px; height: 130px; }

  .hero { position: absolute; left: 0; top: 325px; width: 560px; height: 260px; }

  .maker {
    position: absolute; left: 36px; top: 500px; width: 170px; text-align: center;
    color: var(--ink);
  }
  .maker-name { font-family: "Cormorant Garamond", serif; font-weight: 600; font-size: 28px; letter-spacing: 1px; }
  .maker-sub { font-family: "Cormorant Garamond", serif; font-weight: 600; font-size: 13px; color: var(--brand-green); margin-top: -4px; }

  .product-title {
    position: absolute; left: 52px; top: 594px;
    font-family: "Cormorant Garamond", serif; font-weight: 600; font-size: 58px;
    color: var(--deep-green); letter-spacing: 1px; line-height: 1;
  }
  .title-rule { position: absolute; left: 52px; top: 660px; width: 226px; height: 2px; background: var(--ink); }
  .specs { position: absolute; right: 56px; top: 652px; text-align: right; color: var(--ink); }
  .flavour { font-size: 17px; font-weight: 500; }
  .spec-line { font-size: 11px; line-height: 1.45; }

  .benefits {
    position: absolute; left: 0; right: 0; top: 762px; text-align: center;
    color: var(--brand-green); font-size: 14px; font-weight: 500; letter-spacing: .5px;
  }
  .endorsement {
    position: absolute; left: 0; right: 0; top: 780px; text-align: center;
    color: var(--ink); font-size: 11px;
  }
</style>
</head>
<body>
<main class="canvas">
  <section class="pouch">
    <div class="hang-hole"></div>
    <div class="zip-line"></div>

    <header class="brand-band">
      <h1 class="brand-name">PawVita™</h1>
    </header>

    <svg class="thc-badge" viewBox="0 0 130 130" aria-label="Contains zero THC">
      <g fill="var(--brand-green)">
        <rect x="22" y="22" width="86" height="86" transform="rotate(0 65 65)"/>
        <rect x="22" y="22" width="86" height="86" transform="rotate(15 65 65)"/>
        <rect x="22" y="22" width="86" height="86" transform="rotate(30 65 65)"/>
        <rect x="22" y="22" width="86" height="86" transform="rotate(45 65 65)"/>
        <rect x="22" y="22" width="86" height="86" transform="rotate(60 65 65)"/>
        <rect x="22" y="22" width="86" height="86" transform="rotate(75 65 65)"/>
      </g>
      <circle cx="65" cy="65" r="52" fill="var(--white)"/>
      <circle cx="65" cy="65" r="48" fill="none" stroke="var(--brand-green)" stroke-width="2"/>
      <text x="65" y="48" text-anchor="middle" font-family="Roboto, sans-serif" font-size="14" fill="var(--brand-green)">Contains</text>
      <text x="65" y="74" text-anchor="middle" font-family="Roboto, sans-serif" font-weight="700" font-size="24" fill="var(--brand-green)">ZEERO</text>
      <text x="65" y="98" text-anchor="middle" font-family="Roboto, sans-serif" font-weight="700" font-size="24" fill="var(--brand-green)">THC</text>
    </svg>

    <svg class="hero" viewBox="0 0 560 260">
      <defs>
        <linearGradient id="heroTone" x1="0" y1="0" x2="1" y2="0">
          <stop offset="0" stop-color="#ffffff"/>
          <stop offset="0.35" stop-color="#f0f0ef"/>
          <stop offset="0.7" stop-color="#cfcac6"/>
          <stop offset="1" stop-color="#ececec"/>
        </linearGradient>
      </defs>
      <path d="M14 70 Q 40 40 110 36 L 420 36 Q 540 36 548 100 L 548 205 Q 548 240 510 240 L 60 240 Q 14 240 14 200 Z"
            fill="url(#heroTone)" role="img"
            aria-label="Photo of a white cat nuzzling a wrinkled cream dog wearing a polka-dot bow tie"/>
      <path d="M4 78 Q 40 22 170 22 L 400 22 Q 545 22 556 92"
            fill="none" stroke="var(--brand-green)" stroke-width="12" stroke-linecap="round"/>
    </svg>

    <div class="maker">
      <div class="maker-name">VERDALO</div>
      <div class="maker-sub">For Animals</div>
    </div>

    <h2 class="product-title">CBD TREATS</h2>
    <div class="title-rule"></div>
    <div class="specs">
      <div class="flavour">Flavour: Chicken</div>
      <div class="spec-line">CBD quantity: CBD 250mg</div>
      <div class="spec-line">Net weight: 120g</div>
    </div>

    <p class="benefits">SUPPORT | CALM | EASE</p>
    <p class="endorsement">Social Proof: Recommended by veterinarians</p>
  </section>
</main>
</body>
</html>
```